Norwegian Mobile Home/Cabin Producer Needs Brochure Design

We make and deliver our own brand of mobile homes especially made for Norway and it's weather conditions. We differ from other brands in building quality in regards to a much more solid construction, insulation and choices. We work with our customer from the beginning and build them after their demands and wishes.
We need a brochure that holds us out as top of the line. We deliver mobile homes of all kinds and sizes. Both to the private and professional sector.
For the professional sector, mainly camping sites we want to show, lodges-, sanitary- and kitchen wagoons etc.
So we need a brochure of 14-20 pages in A4 where the double pages can be printed in A3 format.
We have logo (provided). But we need cover as well as back suggestions.
It should start with pages where we can teel who we are and stand for.Piicture(s) and space for some editable text (which we can write in norwegian). The text part can have a transparent background......or not. Give us your best shot. Also a smaller part in the private sector that shows winter time.
We want other pages for the private sector that shows what we deliver and the possibilities of choices.
Pages for the the professional sector.
Pages that show our production. How we transport. And the split construction. Only pictures from this portfolio here. (see fotoskap portfolios)
Take a look at provided pictures and our website www.solvikhytta.no for inspiration.
Here's a FotoSkap link to Pictures to choose from. http://bildelagr.example/K4TQ9P
(Hope it Works, let me know if not)
Our company name in small letters "fjordgrønn hyttebygg" means directly translated "fjordgreen cabin builds".
Looking forward to your suggestions.
Target Market(s)
Private market for vacation mobile homes. Camping sites and similar
Industry/Entity Type
Insulation
Requirements
Must have
- Our logo on the front page. Simple but inviting and professional
Logo and address on the back.

```html
<!DOCTYPE html>
<html lang="no">
<head>
<meta charset="utf-8">
<title>fjordgrønn hyttebygg – brosjyre omslag</title>
<link rel="stylesheet" href="https://fonts.googleapis.com/css2?family=Cormorant+Garamond:wght@400;500&family=Open+Sans:wght@400;700&display=swap">
<style>
  :root {
    --panel: #c9d0e3;
    --band: #7189b5;
    --white: #ffffff;
    --logo-ink: #6a7ea6;
    --address-ink: #2e4570;
    --photo-top: #d9dde2;
    --photo-mid: #8f8a83;
    --photo-low: #5e5650;
  }
  html, body {
    margin: 0;
    padding: 0;
    width: 1200px;
    height: 806px;
    overflow: hidden;
    background: var(--panel);
  }
  .cover-spread {
    position: relative;
    width: 1200px;
    height: 806px;
    background: var(--panel);
  }
  .cover-art {
    position: absolute;
    inset: 0;
  }
  .back-page-info {
    position: absolute;
    left: 30px;
    top: 672px;
  }
  .back-logo-name {
    margin: 0 0 8px;
    font-family: "Cormorant Garamond", serif;
    font-weight: 500;
    font-size: 19px;
    color: var(--logo-ink);
  }
  .back-address {
    margin: 0;
    font-family: "Open Sans", sans-serif;
    font-size: 9px;
    color: var(--address-ink);
  }
  .back-address strong { font-weight: 700; }
  .front-logo-name {
    position: absolute;
    left: 660px;
    top: 672px;
    margin: 0;
    font-family: "Cormorant Garamond", serif;
    font-weight: 500;
    font-size: 38px;
    letter-spacing: 0.5px;
    color: var(--logo-ink);
  }
</style>
</head>
<body>
  <main class="cover-spread">
    <svg class="cover-art" width="1200" height="806" viewBox="0 0 1200 806" aria-hidden="false">
      <defs>
        <linearGradient id="terrace-photo-tones" x1="0" y1="0" x2="0" y2="1">
          <stop offset="0" stop-color="var(--photo-top)"/>
          <stop offset="0.45" stop-color="var(--photo-mid)"/>
          <stop offset="1" stop-color="var(--photo-low)"/>
        </linearGradient>
      </defs>
      <path class="blue-swoosh" fill="var(--band)"
            d="M510,0 C540,330 780,530 1025,511 C1120,504 1170,492 1200,486 L1200,0 Z"/>
      <path class="white-swoosh" fill="var(--white)"
            d="M588,0 C598,310 800,565 1045,583 C810,548 622,300 612,0 Z"/>
      <path class="cover-photo" role="img"
            aria-label="Foto: hytteterrasse ved vannet med hvitt bord og stol, flaske og blomster, båthavn i bakgrunnen"
            fill="url(#terrace-photo-tones)"
            d="M629,0 C650,240 760,440 899,484 C990,500 1100,480 1200,469 L1200,0 Z"/>
    </svg>

    <section class="back-page-info">
      <p class="back-logo-name">fjordgrønn hyttebygg as</p>
      <p class="back-address"><strong>fjordgrønn hyttebygg as,</strong> Postboks 14, 4790 Lillevik | Tel: 40 00 12 34 | Website: www.solvikhytta.no</p>
    </section>

    <h1 class="front-logo-name">fjordgrønn hyttebygg as</h1>
  </main>
</body>
</html>
```